Need App for Impact Related Events

My app is to help with internal events. When you enter the prompted event code the next screen shows you everyone currently at the event. It will give you the ability to Start a conversation with someone you met at that event, or signal it is your turn to send a message. The next screen is a message thread with that person. I am looking for a design that incorporates the colors and ‘feel good’ emotion of our logo. I have pieced together a pretty good interpretation of what I’m looking for in the attached mockup by slicing and dicing designs. I also attached our logo mascot.Screens (see attached mockups)

Note 1: I do not like the picture on the screen used in screen one because it makes it seem like a dating app. I attached an alternative photo that can be used or present different ideas.

Note 2: On the login/signup screen (screen 2) I need an additional first and last name for login, you can try to fit this on one login screen or present a two step signup screen where that is presented in the second screen.

READ MOCKUP GUIDELINES UNDER Must Haves

Target Market(s)

People attending internal social impact events

Industry/Entity Type

Charity

Font styles to use
Sans Serif

Colors
86cfc6

Requirements
Must have
• Follow the screen mockups attached to project
• PLEASE READ
• I have provided a relatively close design of what I’m looking for in the mockups. Some screens need to be followed more closely to my design mockup than other. I have listed a guide below how how closely you should follow my mockup design exactly. Overall I would like to see some ideas of incorporating a few accent colors so it doesn’t appear SO Blue. I also attached some app inspiration designs I found from around the web
• Screen Mockup Guideline Follow %
• Screen 1: 65% - mostly on target, would like to see ways to make it not SO Blue and possibly creative places to add some explainer text describing the app
• Screen 2: 50% - general design idea is here, but more open
• Screen 3: 35% - a lot more room for design influence
• Screen 4: 70% - mostly on target, a little room for design influence/color scheme ideas
• Screen 5-6: 25% - a lot of room for design change/ideas/influence
• Screen 7-8: 80% - already very close to what I need, maybe open to slight sizing and color scheme ideas
• Screen 9: 15% - the most open for influence, only the general functionality of the screen is communicated here
Nice to have
• Please Read Mockup Guideline above. In large part I am looking for something to use some nice accent colors so it is not overwhelmingly blue and bring the whole design into a seamless style.
Should not have

```html
<!DOCTYPE html>
<html lang="en">
<head>
<meta charset="utf-8">
<title>Enter Code – Hello Circle</title>
<link rel="stylesheet" href="https://fonts.googleapis.com/css2?family=Inter:wght@400;500;600&display=swap">
<style>
  :root {
    --bg: #ffffff;
    --screen: #f7f7f8;
    --surface: #ffffff;
    --ink: #1c2d3d;
    --ink-soft: #2b2f36;
    --muted: #a4abb3;
    --rule: #e4e6e9;
    --teal: #2ff0da;
    --teal-deep: #1fcfbd;
    --teal-line: #34d6c6;
    --teal-text: #2ee3d2;
    --photo-top: #6f8d96;
    --photo-mid: #5aa7a6;
    --photo-bottom: #3de6cf;
    --kb-bg: #d2d5db;
    --kb-key: #ffffff;
    --kb-key-dark: #abb0ba;
  }
  * { box-sizing: border-box; margin: 0; padding: 0; }
  html, body { width: 1200px; height: 1200px; overflow: hidden; }
  body {
    background: var(--bg);
    font-family: "Inter", "Helvetica Neue", Arial, sans-serif;
    color: var(--ink);
    position: relative;
  }
  .screen {
    position: absolute;
    top: 180px;
    width: 390px;
    height: 840px;
    background: var(--screen);
    border-radius: 40px;
    overflow: hidden;
    box-shadow: 0 0 0 1px #e2e4e7;
  }
  .screen--empty { left: 140px; }
  .screen--typing { left: 670px; }

  .status-bar {
    position: absolute; top: 0; left: 0; right: 0; height: 48px;
    background: var(--surface);
  }
  .status-bar__time {
    position: absolute; left: 36px; top: 18px;
    font-size: 14px; font-weight: 600; color: #111;
  }
  .status-bar__icons { position: absolute; right: 24px; top: 20px; }

  .nav-bar {
    position: absolute; top: 48px; left: 0; right: 0; height: 45px;
    background: var(--surface);
    border-bottom: 1px solid var(--rule);
  }
  .nav-bar__back { position: absolute; left: 16px; top: 10px; }
  .nav-bar__title {
    position: absolute; left: 0; right: 0; top: 11px;
    text-align: center; font-size: 16px; color: var(--ink-soft);
  }

  .code-card {
    position: absolute; left: 16px; top: 117px; width: 357px;
    background: var(--surface);
    border-radius: 8px;
    overflow: hidden;
  }
  .screen--empty .code-card { height: 368px; }
  .screen--typing .code-card { height: 324px; }

  .code-card__photo {
    position: relative; width: 100%;
    background: linear-gradient(180deg, var(--photo-top) 0%, var(--photo-mid) 55%, var(--photo-bottom) 100%);
  }
  .screen--empty .code-card__photo { height: 235px; }
  .screen--typing .code-card__photo { height: 194px; }

  .brand {
    position: absolute; left: 20px; bottom: 10px;
    display: flex; align-items: center; gap: 10px;
  }
  .brand__dot {
    width: 46px; height: 46px; border-radius: 50%;
    background: var(--surface);
  }
  .brand__name { font-size: 21px; font-weight: 500; color: var(--ink); }

  .code-field { position: absolute; left: 21px; right: 21px; }
  .code-field__label { font-size: 17px; font-weight: 500; color: var(--ink); }
  .code-field__input {
    margin-top: 20px; font-size: 19px; padding-bottom: 12px;
    border-bottom: 1.5px solid var(--teal-line);
  }
  .code-field__input--placeholder { color: var(--muted); }
  .code-field__input--filled { color: var(--teal-text); }
  .screen--empty .code-field { top: 255px; }
  .screen--typing .code-field { top: 214px; }

  .submit-button {
    position: absolute; left: 70px; width: 249px; height: 53px;
    background: var(--teal);
    border-radius: 4px;
    border-bottom: 3px solid var(--teal-deep);
    color: #fff; font-size: 17px; font-weight: 500; letter-spacing: 0.2px;
    display: flex; align-items: center; justify-content: center;
  }
  .screen--empty .submit-button { top: 531px; }
  .screen--typing .submit-button { top: 464px; }

  .create-link {
    position: absolute; left: 0; right: 0; top: 780px;
    text-align: center; font-size: 24px; font-weight: 500; color: var(--ink);
  }

  .keyboard {
    position: absolute; left: 0; right: 0; top: 540px; bottom: 0;
    background: var(--kb-bg);
    padding: 8px 3px 0;
    font-family: "Inter", "Helvetica Neue", Arial, sans-serif;
  }
  .keyboard__row { display: flex; justify-content: center; gap: 5px; margin-bottom: 12px; }
  .key {
    height: 43px; width: 34px;
    background: var(--kb-key);
    border-radius: 5px;
    box-shadow: 0 1px 0 #8f949c;
    display: flex; align-items: center; justify-content: center;
    font-size: 22px; color: #111;
  }
  .key--dark { background: var(--kb-key-dark); }
  .key--wide { width: 44px; }
  .key--label { font-size: 16px; }
  .key--num { width: 89px; }
  .key--space { width: 99px; }
  .key--at { width: 43px; }
  .key--dot { width: 43px; }
  .key--return { width: 90px; }
  .keyboard__row--letters-2 { padding: 0 20px; }
  .keyboard__row--letters-3 { justify-content: space-between; padding: 0 2px; }
  .keyboard__row--letters-3 .letters { display: flex; gap: 5px; }
  .keyboard__footer { position: absolute; left: 28px; right: 36px; top: 240px; display: flex; justify-content: space-between; }
  .home-indicator {
    position: absolute; left: 125px; width: 140px; bottom: 10px; height: 5px;
    border-radius: 3px; background: #111;
  }
</style>
</head>
<body>

  <section class="screen screen--empty">
    <div class="status-bar">
      <span class="status-bar__time">9:41</span>
      <svg class="status-bar__icons" width="48" height="12" viewBox="0 0 48 12">
        <path d="M9 11 L6 8 A4.5 4.5 0 0 1 12 8 Z M3.5 5.5 A8 8 0 0 1 14.5 5.5 L13 7 A6 6 0 0 0 5 7 Z M1 3 A11.5 11.5 0 0 1 17 3 L15.6 4.4 A9.5 9.5 0 0 0 2.4 4.4 Z" fill="#111"/>
        <rect x="23" y="1" width="21" height="10" rx="2.5" fill="none" stroke="#111" stroke-width="1"/>
        <rect x="25" y="3" width="17" height="6" rx="1" fill="#111"/>
        <rect x="45" y="4" width="1.5" height="4" fill="#111"/>
      </svg>
    </div>
    <header class="nav-bar">
      <svg class="nav-bar__back" width="14" height="24" viewBox="0 0 14 24"><path d="M12 2 L3 12 L12 22" fill="none" stroke="#2b2f36" stroke-width="2.4" stroke-linecap="round" stroke-linejoin="round"/></svg>
      <h1 class="nav-bar__title">Enter&nbsp; Code</h1>
    </header>

    <div class="code-card">
      <div class="code-card__photo" role="img" aria-label="Photo of friends chatting over coffee at a café table, tinted teal">
        <div class="brand"><span class="brand__dot"></span><span class="brand__name">Hello Circle</span></div>
      </div>
      <div class="code-field">
        <p class="code-field__label">Enter location kind code</p>
        <p class="code-field__input code-field__input--placeholder">Enter Code</p>
      </div>
    </div>

    <div class="submit-button">SUBMIT</div>
    <p class="create-link">Create a Kind Code</p>
  </section>

  <section class="screen screen--typing">
    <div class="status-bar">
      <span class="status-bar__time">9:41</span>
      <svg class="status-bar__icons" width="48" height="12" viewBox="0 0 48 12">
        <path d="M9 11 L6 8 A4.5 4.5 0 0 1 12 8 Z M3.5 5.5 A8 8 0 0 1 14.5 5.5 L13 7 A6 6 0 0 0 5 7 Z M1 3 A11.5 11.5 0 0 1 17 3 L15.6 4.4 A9.5 9.5 0 0 0 2.4 4.4 Z" fill="#111"/>
        <rect x="23" y="1" width="21" height="10" rx="2.5" fill="none" stroke="#111" stroke-width="1"/>
        <rect x="25" y="3" width="17" height="6" rx="1" fill="#111"/>
        <rect x="45" y="4" width="1.5" height="4" fill="#111"/>
      </svg>
    </div>
    <header class="nav-bar">
      <svg class="nav-bar__back" width="14" height="24" viewBox="0 0 14 24"><path d="M12 2 L3 12 L12 22" fill="none" stroke="#2b2f36" stroke-width="2.4" stroke-linecap="round" stroke-linejoin="round"/></svg>
      <h1 class="nav-bar__title">Enter&nbsp; Code</h1>
    </header>

    <div class="code-card">
      <div class="code-card__photo" role="img" aria-label="Photo of friends chatting over coffee at a café table, tinted teal">
        <div class="brand"><span class="brand__dot"></span><span class="brand__name">Hello Circle</span></div>
      </div>
      <div class="code-field">
        <p class="code-field__label">Enter location kind code</p>
        <p class="code-field__input code-field__input--filled">AA4367CN6734</p>
      </div>
    </div>

    <div class="submit-button">SUBMIT</div>

    <div class="keyboard">
      <div class="keyboard__row">
        <span class="key">q</span><span class="key">w</span><span class="key">e</span><span class="key">r</span><span class="key">t</span><span class="key">y</span><span class="key">u</span><span class="key">i</span><span class="key">o</span><span class="key">p</span>
      </div>
      <div class="keyboard__row keyboard__row--letters-2">
        <span class="key">a</span><span class="key">s</span><span class="key">d</span><span class="key">f</span><span class="key">g</span><span class="key">h</span><span class="key">j</span><span class="key">k</span><span class="key">l</span>
      </div>
      <div class="keyboard__row keyboard__row--letters-3">
        <span class="key key--dark key--wide">
          <svg width="20" height="18" viewBox="0 0 20 18"><path d="M10 1 L19 10 H14 V17 H6 V10 H1 Z" fill="none" stroke="#111" stroke-width="1.4" stroke-linejoin="round"/></svg>
        </span>
        <span class="letters">
          <span class="key">z</span><span class="key">x</span><span class="key">c</span><span class="key">v</span><span class="key">b</span><span class="key">n</span><span class="key">m</span>
        </span>
        <span class="key key--dark key--wide">
          <svg width="24" height="16" viewBox="0 0 24 16"><path d="M7 1 H22 V15 H7 L1 8 Z M11 5 L17 11 M17 5 L11 11" fill="none" stroke="#111" stroke-width="1.4" stroke-linejoin="round"/></svg>
        </span>
      </div>
      <div class="keyboard__row">
        <span class="key key--dark key--label key--num">123</span>
        <span class="key key--label key--space">space</span>
        <span class="key key--at">@</span>
        <span class="key key--dot">.</span>
        <span class="key key--dark key--label key--return">return</span>
      </div>
      <div class="keyboard__footer">
        <svg width="28" height="28" viewBox="0 0 28 28"><circle cx="14" cy="14" r="12.5" fill="none" stroke="#555" stroke-width="1.5"/><circle cx="10" cy="11" r="1.5" fill="#555"/><circle cx="18" cy="11" r="1.5" fill="#555"/><path d="M8 16 Q14 22 20 16" fill="none" stroke="#555" stroke-width="1.5"/></svg>
        <svg width="18" height="28" viewBox="0 0 18 28"><rect x="5" y="1" width="8" height="16" rx="4" fill="none" stroke="#555" stroke-width="1.5"/><path d="M2 13 A7 7 0 0 0 16 13 M9 20 V26 M5 26 H13" fill="none" stroke="#555" stroke-width="1.5"/></svg>
      </div>
      <span class="home-indicator"></span>
    </div>
  </section>

</body>
</html>
```